Trendy Stylish Safety/Sports glasses polybag and box packaging

Polybag artwork required for safety glasses.
Polybag artwork required for sports glasses.
Packing box artwork required to tie in with polybag packaging.

Both bags to be similar, however one for safety glasses and one for sports glasses.
Maybe touch of different colours to differentiate.

Polybag Packaging for safety glasses.
1. Text to be white on black or vice versa, with a touch of yellow
2. Kermo logos to use, attached.
3. Front of bag to have clear vision panel on RH side
4. Bullet points can be on this clear vision panel.
5. Strapline to be on front of bag after ‘kerMosafety’ is COMFORT…STYLE…PROTECTION
6. Happy to have a touch of other colours on the packet to brighten up, make distinctive.
7. RH side at top on reverse of bag, bar code label to be attached, so this section to be left clear
8. Could have a few safety symbols on possibly.
9. Full text required on polybag is in file ‘safety packaging bag info.docx’

Polybag packaging for sports glasses

1. Text to be white on black or vice versa, with a touch of blue
5. Strapline to be on front of bag after ‘kerMosports’ is PERFORMANCE.…STYLE…PROTECTION
8. Full text required on polybag is in file ‘SPORTS packaging BAG Details.docx’
We havent decided on text for the reverse of this bag, however once we have the basic layout, we can add text at a later stage.

Cardboard packing/posting box for case.

We will use these boxes to pack and despatch our sports and safety glasses.

1. Two long sides of box to match polybag kerMo safety design.
Text required on safety sides of box
kerMosafety logo
COMFORT, STYLE, PROTECTION
2. Two long sides of box to match polybag kerMo sports design.
3. Text required on sports sides of box
kerMosports logo
PERFORMANCE, STYLE, PROTECTION
4. case box jpg has sizes required
Example of packing box picture attached.

Industry/Entity Type

Safety

```html
<!DOCTYPE html>
<html lang="en">
<head>
<meta charset="utf-8">
<title>kerMo safety and sports packaging</title>
<link rel="stylesheet" href="https://fonts.googleapis.com/css2?family=Michroma&family=Open+Sans:wght@400;700&display=swap">
<style>
  :root{
    --yellow:#fff200;
    --blue:#00aeef;
    --ink:#231f20;
    --paper:#ffffff;
    --wide:"Michroma",sans-serif;
    --body:"Open Sans",sans-serif;
  }
  html,body{margin:0;padding:0;overflow:hidden;background:var(--paper);}
  .canvas{display:block;width:1200px;height:1067px;}
  .theme-safety{--accent:var(--yellow);}
  .theme-sports{--accent:var(--blue);}
  .fill-accent{fill:var(--accent);}
  .fill-ink{fill:var(--ink);}
  .fill-paper{fill:var(--paper);}
  .stop-yellow{stop-color:var(--yellow);}
  .stop-blue{stop-color:var(--blue);}
  .stop-ink{stop-color:var(--ink);}
  .range-title{font-family:var(--wide);font-size:40px;fill:var(--ink);}
  .brand-name{font-family:var(--wide);fill:var(--paper);}
  .brand-ink{fill:var(--ink);}
  .brand-accent{fill:var(--accent);}
  .strapline{font-family:var(--wide);font-size:6px;letter-spacing:1.2px;fill:var(--accent);}
  .strapline-back{font-family:var(--wide);font-size:8.5px;letter-spacing:2px;fill:var(--paper);}
  .web-address{font-family:var(--body);font-size:5px;fill:var(--paper);}
  .feature-list{font-family:var(--wide);font-size:5px;letter-spacing:0.6px;fill:var(--ink);}
  .box-strapline{font-family:var(--wide);font-size:7.5px;letter-spacing:1.2px;fill:var(--accent);}
  .box-strapline-long{font-size:6px;letter-spacing:0.8px;}
  .back-copy{font-family:var(--body);font-size:4.4px;line-height:1.35;color:var(--ink);margin:0;padding:10px 10px 0 10px;}
  .back-copy h4{font-size:4.6px;text-align:center;margin:0 0 4px;}
  .back-copy p{margin:0 0 7px;}
  .back-copy b{font-weight:700;}
  .marking-table{border-collapse:collapse;width:100%;margin:0 0 8px;}
  .marking-table td{border:0.4px solid var(--ink);padding:1.5px 2px;vertical-align:top;}
  .sports-copy{font-family:var(--body);font-size:5.3px;line-height:1.5;color:var(--ink);padding:14px 12px 0 12px;margin:0;}
  .sports-copy ul{margin:8px 0 10px;padding-left:12px;}
  .sports-copy p{margin:0 0 8px;}
  .sports-copy .indented{padding-left:14px;}
</style>
</head>
<body>
<svg class="canvas" viewBox="0 0 1200 1067" xmlns="http://www.w3.org/2000/svg">
  <defs>
    <linearGradient id="strip-safety" x1="0" y1="0" x2="0" y2="1">
      <stop offset="0.3" class="stop-ink"/><stop offset="1" class="stop-yellow"/>
    </linearGradient>
    <linearGradient id="strip-sports" x1="0" y1="0" x2="0" y2="1">
      <stop offset="0.15" class="stop-ink"/><stop offset="1" class="stop-blue"/>
    </linearGradient>
    <linearGradient id="side-safety" x1="0" y1="0" x2="1" y2="1">
      <stop offset="0.25" class="stop-yellow"/><stop offset="0.75" class="stop-ink"/>
    </linearGradient>
    <linearGradient id="side-sports" x1="0" y1="0" x2="1" y2="1">
      <stop offset="0.25" class="stop-blue"/><stop offset="0.75" class="stop-ink"/>
    </linearGradient>
    <linearGradient id="edge-safety" x1="0" y1="0" x2="1" y2="0">
      <stop offset="0" class="stop-yellow"/><stop offset="0.45" class="stop-ink"/>
    </linearGradient>
    <linearGradient id="edge-sports" x1="0" y1="0" x2="1" y2="0">
      <stop offset="0" class="stop-blue"/><stop offset="0.45" class="stop-ink"/>
    </linearGradient>
  </defs>

  <!-- ================= SAFETY ================= -->
  <g class="theme-safety">
    <text class="range-title" transform="translate(128 388) rotate(-90)" textLength="238" lengthAdjust="spacing">SAFETY</text>

    <!-- polybag front -->
    <g class="bag-front" transform="translate(147 45)">
      <rect width="173" height="457" class="fill-ink"/>
      <path class="fill-accent" d="M0 0H173V4C120 10 90 30 60 55C40 72 20 80 0 84Z"/>
      <rect class="halftone" role="img" aria-label="Halftone dot fade in yellow" x="0" y="84" width="58" height="373" fill="url(#strip-safety)"/>
      <rect class="clear-window fill-paper" x="58" y="80" width="115" height="315"/>
      <text class="brand-name" x="22" y="62" font-size="11">kerMosafety</text>
      <g transform="translate(0 165) rotate(-90)">
        <text class="strapline" x="0" y="20">COMFORT</text>
        <text class="strapline" x="0" y="31">STYLE</text>
        <text class="strapline" x="0" y="42">PROTECTION</text>
      </g>
      <text class="brand-name" font-size="24" transform="translate(44 395) rotate(-90)">kerMo</text>
      <g class="feature-list">
        <text x="64" y="331">• IMPACT RESISTANT</text>
        <text x="64" y="341">• STYLISH DESIGN</text>
        <text x="64" y="351">• CE CERTIFIED</text>
        <text x="64" y="361">• POLYCARBONATE LENS</text>
        <text x="64" y="371">• UV PROTECTION</text>
        <text x="64" y="381">• ANTI FOG COATED</text>
      </g>
    </g>

    <!-- polybag back -->
    <g class="bag-back" transform="translate(330 45)">
      <rect width="173" height="457" class="fill-ink"/>
      <path class="fill-accent" d="M50 0H173V70C150 40 110 15 50 0Z"/>
      <text class="web-address" x="12" y="35">www.kermosafety.com</text>
      <text class="strapline-back" x="12" y="47">COMFORT</text>
      <text class="strapline-back" x="12" y="60">STYLE</text>
      <text class="strapline-back" x="12" y="73">PROTECTION</text>
      <rect class="fill-paper" x="0" y="77" width="173" height="325"/>
      <foreignObject x="0" y="77" width="173" height="325">
        <div xmlns="http://www.w3.org/1999/xhtml" class="back-copy">
          <h4>EN166:2001</h4>
          <p><b>Taking care of your safety eyewear:</b> Store at normal room temperature in a box or locker. Transport in the box, bag or case provided and not unprotected with other items. Clean with warm soapy water, rinse then dry with a clean lint free cloth or tissue. Disinfect when required with mild household or medical disinfectant, then rinse off and dry. Check daily hinges, pivots and moving parts for tightness and security. Broken products, scratched lenses and items obviously at the end of their useful life must be immediately replaced.</p>
          <p><b>Product Life:</b> If stored in good condition at an even ambient temperature they will last in excess of 2 years but must be thoroughly inspected before use. If there are any signs of deterioration they should be replaced.</p>
          <p><b>Product Markings:</b> If the symbols S, F or B are not common to both ocular and the frame, then it is the lower level that shall be assigned to the complete eye protector.</p>
          <table class="marking-table">
            <tr><td>SYMBOL</td><td>DESCRIPTION OF THE FIELD OF USE/MARKINGS</td></tr>
            <tr><td>No symbol</td><td>General purpose, low speed impacts (frame only)</td></tr>
            <tr><td>S</td><td>Increased robustness</td></tr>
            <tr><td>F</td><td>High speed particles, Low energy impact</td></tr>
            <tr><td>B</td><td>High speed particles, Medium energy impact</td></tr>
            <tr><td>1</td><td>Optical class 1</td></tr>
            <tr><td>EN166</td><td>European standard number for Personal Eye Protection</td></tr>
          </table>
          <p><b>Warning:</b> Impacts may be transmitted to eyewear worn underneath, thus creating a hazard. Applicable at room temperature only unless marked with the letter T. Should the product cause skin irritation its use should be discontinued and medical advice sought.</p>
          <p>Additional markings for filtered lenses: shade numbers are shown before the maker's mark. EN170 ultra violet filters, EN171 infrared filters, EN172 sun glare filters.<br>Made in Taiwan</p>
        </div>
      </foreignObject>
    </g>

    <!-- packing box -->
    <g class="box-net" transform="translate(60 535)">
      <path class="fill-accent" d="M28 30V12Q28 0 40 0H150Q162 0 162 12V30Z"/>
      <rect x="28" y="30" width="134" height="97" class="fill-ink"/>
      <rect x="162" y="65" width="100" height="62" class="fill-accent"/>
      <polygon class="fill-accent" points="262,127 290,65 372,65 398,127"/>
      <polygon class="fill-accent" points="398,127 422,65 498,65 498,127"/>
      <polygon role="img" aria-label="Yellow halftone fade into black" points="0,140 28,127 162,127 162,420 28,420 0,405" fill="url(#side-safety)"/>
      <rect x="162" y="127" width="100" height="293" class="fill-ink"/>
      <rect role="img" aria-label="Halftone dot edge in yellow" x="262" y="127" width="136" height="293" fill="url(#edge-safety)"/>
      <rect x="398" y="127" width="100" height="293" class="fill-ink"/>
      <polygon class="fill-accent" points="28,420 162,420 162,520 112,520 98,482 84,520 28,520"/>
      <polygon class="fill-accent" points="162,420 262,420 262,470 246,520 180,520 162,470"/>
      <polygon class="fill-accent" points="262,420 398,420 398,520 350,520 330,482 310,520 262,520"/>
      <polygon class="fill-accent" points="398,420 498,420 498,520 420,520 398,470"/>
      <text class="brand-name brand-ink" font-size="30" transform="translate(70 300) rotate(-65)">kerMo</text>
      <text class="brand-name brand-accent" font-size="30" transform="translate(300 365) rotate(-65)">kerMo</text>
      <g transform="translate(162 232) rotate(-90)">
        <text class="box-strapline" x="0" y="42">COMFORT</text>
        <text class="box-strapline" x="0" y="56">STYLE</text>
        <text class="box-strapline" x="0" y="70">PROTECTION</text>
      </g>
      <text class="brand-name" font-size="13" transform="translate(222 395) rotate(-90)">kerMosafety</text>
      <g transform="translate(398 232) rotate(-90)">
        <text class="box-strapline" x="0" y="42">COMFORT</text>
        <text class="box-strapline" x="0" y="56">STYLE</text>
        <text class="box-strapline" x="0" y="70">PROTECTION</text>
      </g>
      <text class="brand-name" font-size="13" transform="translate(458 395) rotate(-90)">kerMosafety</text>
    </g>
  </g>

  <!-- ================= SPORTS ================= -->
  <g class="theme-sports">
    <text class="range-title" transform="translate(716 385) rotate(-90)" textLength="255" lengthAdjust="spacing">SPORTS</text>

    <g class="bag-front" transform="translate(733 45)">
      <rect width="173" height="457" class="fill-ink"/>
      <path class="fill-accent" d="M0 0H173V4C120 10 90 30 60 55C40 72 20 80 0 84Z"/>
      <rect role="img" aria-label="Halftone dot fade in blue" x="0" y="84" width="58" height="373" fill="url(#strip-sports)"/>
      <rect class="clear-window fill-paper" x="58" y="80" width="115" height="315"/>
      <text class="brand-name" x="22" y="62" font-size="11">kerMosports</text>
      <g transform="translate(0 178) rotate(-90)">
        <text class="strapline" x="0" y="20">PERFORMANCE</text>
        <text class="strapline" x="0" y="31">STYLE</text>
        <text class="strapline" x="0" y="42">PROTECTION</text>
      </g>
      <text class="brand-name" font-size="24" transform="translate(44 395) rotate(-90)">kerMo</text>
      <g class="feature-list">
        <text x="64" y="329">• IMPACT RESISTANT</text>
        <text x="64" y="339">• STYLISH DESIGN</text>
        <text x="64" y="349">• CE CERTIFIED</text>
        <text x="64" y="359">• POLYCARBONATE LENS</text>
        <text x="64" y="369">• UV PROTECTION</text>
        <text x="64" y="379">• ANTI FOG COATED</text>
      </g>
    </g>

    <g class="bag-back" transform="translate(918 45)">
      <rect width="173" height="457" class="fill-ink"/>
      <path class="fill-accent" d="M50 0H173V70C150 40 110 15 50 0Z"/>
      <text class="web-address" x="12" y="33">www.kermosports.com</text>
      <text class="strapline-back" x="12" y="45">PERFORMANCE</text>
      <text class="strapline-back" x="12" y="58">STYLE</text>
      <text class="strapline-back" x="12" y="71">PROTECTION</text>
      <rect class="fill-paper" x="0" y="77" width="173" height="318"/>
      <foreignObject x="0" y="77" width="173" height="318">
        <div xmlns="http://www.w3.org/1999/xhtml" class="sports-copy">
          <p>PERFORMANCE STYLISH SPORTS GLASSES</p>
          <ul>
            <li>RUNNING</li><li>CYCLING</li><li>SKIING</li><li>ATHLETICS</li><li>FISHING</li><li>GOLF<br>Etc etc</li>
          </ul>
          <p class="indented">MEETS OR EXCEEDS ALL CE STANDARDS FOR UV PROTECTION AND FRAME PROTECTION&gt; BLAH BLAH</p>
          <p class="indented">Ugzvnod;asfgioad;b<br>Iagve;oinv ofg'v;p's\v<br>lagnvclsgnv;nao;gnv<br>Usagvo;nsgvl;c o;jgvo\sp<br>Ugzvnod;asfgioad;b<br>Iagve;oinv ofg'v;p's\v<br>lagnvclsgnv;nao;gnv<br>Usagvo;nsgvl;c o;jgvo\sp<br>Ugzvnod;asfgioad;b<br>Iagve;oinv ofg'v;p's\v<br>lagnvclsgnv;nao;gnv<br>Usagvo;nsgvl;c o;jgvo\sp</p>
        </div>
      </foreignObject>
    </g>

    <g class="box-net" transform="translate(637 535)">
      <path class="fill-accent" d="M28 30V12Q28 0 40 0H150Q162 0 162 12V30Z"/>
      <rect x="28" y="30" width="134" height="97" class="fill-ink"/>
      <rect x="162" y="65" width="100" height="62" class="fill-accent"/>
      <polygon class="fill-accent" points="262,127 290,65 372,65 398,127"/>
      <polygon class="fill-accent" points="398,127 422,65 498,65 498,127"/>
      <polygon role="img" aria-label="Blue halftone fade into black" points="0,140 28,127 162,127 162,420 28,420 0,405" fill="url(#side-sports)"/>
      <rect x="162" y="127" width="100" height="293" class="fill-ink"/>
      <rect role="img" aria-label="Halftone dot edge in blue" x="262" y="127" width="136" height="293" fill="url(#edge-sports)"/>
      <rect x="398" y="127" width="100" height="293" class="fill-ink"/>
      <polygon class="fill-accent" points="28,420 162,420 162,520 112,520 98,482 84,520 28,520"/>
      <polygon class="fill-accent" points="162,420 262,420 262,470 246,520 180,520 162,470"/>
      <polygon class="fill-accent" points="262,420 398,420 398,520 350,520 330,482 310,520 262,520"/>
      <polygon class="fill-accent" points="398,420 498,420 498,520 420,520 398,470"/>
      <text class="brand-name brand-ink" font-size="30" transform="translate(70 300) rotate(-65)">kerMo</text>
      <text class="brand-name brand-accent" font-size="30" transform="translate(300 365) rotate(-65)">kerMo</text>
      <g transform="translate(162 222) rotate(-90)">
        <text class="box-strapline box-strapline-long" x="0" y="44">PERFORMANCE</text>
        <text class="box-strapline box-strapline-long" x="0" y="56">STYLE</text>
        <text class="box-strapline box-strapline-long" x="0" y="68">PROTECTION</text>
      </g>
      <text class="brand-name" font-size="13" transform="translate(222 395) rotate(-90)">kerMosports</text>
      <g transform="translate(398 222) rotate(-90)">
        <text class="box-strapline box-strapline-long" x="0" y="44">PERFORMANCE</text>
        <text class="box-strapline box-strapline-long" x="0" y="56">STYLE</text>
        <text class="box-strapline box-strapline-long" x="0" y="68">PROTECTION</text>
      </g>
      <text class="brand-name" font-size="13" transform="translate(458 395) rotate(-90)">kerMosports</text>
    </g>
  </g>
</svg>
</body>
</html>
```